iOS7 test prep app

I need 3 basic screens and 2 product images for an iOS7 app I am prototyping. I provided lots of detail in the attached brief. This is an education product, so warm colors (especially reds) work best.

If you've done flat design for mobile products, please take a look ... Thanks!

Greetings, all. Thank you for your submissions. I am meeting with my product development team this week to review your submissions, and will select a designer before the end of the week. I appreciate your patience with my process, and thank you again for your interest in my project. I'll be back to you soon ... -Dorian

```html
<!DOCTYPE html>
<html lang="en">
<head>
<meta charset="utf-8">
<title>Kestrel Prep – Menu</title>
<link rel="stylesheet" href="https://fonts.googleapis.com/css2?family=Inter:wght@600;700&family=Roboto+Condensed:wght@400;700&display=swap">
<style>
  :root {
    --status-bg: #000000;
    --status-text: #f2f2f2;
    --header-red: #ee1c25;
    --header-text: #ffffff;
    --photo-shade: rgba(58, 58, 58, 0.62);
    --button-dark: rgba(38, 38, 38, 0.86);
    --button-active: rgba(22, 158, 48, 0.88);
    --button-text: #ffffff;
  }
  * { box-sizing: border-box; margin: 0; padding: 0; }
  html, body {
    width: 1200px;
    height: 2250px;
    overflow: hidden;
    background: #000;
  }
  .app-screen {
    position: relative;
    width: 1200px;
    height: 2250px;
    overflow: hidden;
  }
  .status-bar {
    position: absolute;
    top: 0; left: 0;
    width: 100%;
    height: 75px;
    background: var(--status-bg);
    color: var(--status-text);
    font-family: "Inter", sans-serif;
    font-weight: 700;
    display: flex;
    align-items: center;
    padding: 0 24px;
  }
  .status-carrier {
    display: flex;
    align-items: center;
    gap: 8px;
    font-size: 42px;
  }
  .status-time {
    position: absolute;
    left: 50%;
    transform: translateX(-50%);
    font-size: 44px;
  }
  .status-icons {
    margin-left: auto;
    display: flex;
    align-items: center;
    gap: 22px;
  }
  .app-header {
    position: absolute;
    top: 75px; left: 0;
    width: 100%;
    height: 188px;
    background: var(--header-red);
    display: flex;
    align-items: center;
    justify-content: center;
  }
  .app-title {
    font-family: "Roboto Condensed", sans-serif;
    font-weight: 700;
    font-size: 88px;
    color: var(--header-text);
    letter-spacing: -0.5px;
  }
  .backdrop-photo {
    position: absolute;
    top: 263px; left: 0;
    width: 100%;
    height: 1987px;
    background:
      radial-gradient(ellipse at 45% 20%, #c9a98e 0%, rgba(201,169,142,0) 45%),
      radial-gradient(ellipse at 60% 55%, #b88e5e 0%, rgba(184,142,94,0) 50%),
      radial-gradient(ellipse at 20% 40%, #a4663f 0%, rgba(164,102,63,0) 40%),
      linear-gradient(180deg, #d9d9d9 0%, #b9a692 40%, #c8b9a8 75%, #e2ddd6 100%);
  }
  .backdrop-shade {
    position: absolute;
    top: 263px; left: 0;
    width: 100%;
    height: 1987px;
    background: var(--photo-shade);
  }
  .main-menu {
    position: absolute;
    top: 607px;
    left: 75px;
    width: 1085px;
    list-style: none;
    display: flex;
    flex-direction: column;
    gap: 56px;
  }
  .menu-item {
    height: 150px;
    border-radius: 75px;
    background: var(--button-dark);
    display: flex;
    align-items: center;
    padding-left: 108px;
    font-family: "Roboto Condensed", sans-serif;
    font-weight: 400;
    font-size: 53px;
    color: var(--button-text);
  }
  .menu-item.is-active { background: var(--button-active); }
</style>
</head>
<body>
<main class="app-screen">
  <header class="status-bar">
    <div class="status-carrier">
      <svg width="62" height="30" viewBox="0 0 62 30" aria-hidden="true">
        <rect x="0" y="20" width="9" height="10" fill="#f2f2f2"/>
        <rect x="12" y="15" width="9" height="15" fill="#f2f2f2"/>
        <rect x="24" y="10" width="9" height="20" fill="#f2f2f2"/>
        <rect x="36" y="5" width="9" height="25" fill="#f2f2f2"/>
        <rect x="48" y="0" width="9" height="30" fill="#f2f2f2"/>
      </svg>
      <span>Nova</span>
    </div>
    <div class="status-time">4:20 PM</div>
    <div class="status-icons">
      <svg width="34" height="34" viewBox="0 0 34 34" aria-hidden="true">
        <circle cx="17" cy="17" r="16" fill="#f2f2f2"/>
        <path d="M17 7 V17 H24" stroke="#000" stroke-width="3.5" fill="none"/>
      </svg>
      <svg width="38" height="38" viewBox="0 0 38 38" aria-hidden="true">
        <path d="M36 2 L2 17 L19 19 L21 36 Z" fill="#f2f2f2"/>
      </svg>
      <svg width="56" height="52" viewBox="0 0 56 52" aria-hidden="true">
        <path d="M46 14 A22 22 0 1 0 48 34" stroke="#f2f2f2" stroke-width="4.5" fill="none"/>
        <path d="M40 30 L48 40 L55 29 Z" fill="#f2f2f2"/>
        <rect x="16" y="23" width="20" height="15" rx="2" fill="#f2f2f2"/>
        <path d="M20 23 V18 A6 6 0 0 1 32 18 V23" stroke="#f2f2f2" stroke-width="3.5" fill="none"/>
      </svg>
      <svg width="80" height="34" viewBox="0 0 80 34" aria-hidden="true">
        <rect x="2" y="2" width="68" height="30" rx="3" stroke="#f2f2f2" stroke-width="3" fill="none"/>
        <rect x="7" y="7" width="58" height="20" fill="#f2f2f2"/>
        <rect x="72" y="11" width="6" height="12" fill="#f2f2f2"/>
      </svg>
    </div>
  </header>

  <div class="app-header">
    <h1 class="app-title">Kestrel Prep</h1>
  </div>

  <div class="backdrop-photo" role="img" aria-label="Blurred photo of a smiling family with their golden retriever"></div>
  <div class="backdrop-shade"></div>

  <nav>
    <ul class="main-menu">
      <li class="menu-item is-active">HOME</li>
      <li class="menu-item">ABOUT US</li>
      <li class="menu-item">PRODUCT</li>
      <li class="menu-item">STUDENTS</li>
      <li class="menu-item">QUESTIONS</li>
      <li class="menu-item">CONTACT US</li>
    </ul>
  </nav>
</main>
</body>
</html>
```